Flyer, Anzeige & Aufkleber für Massagen gestalten
Zielgruppe
Massage. Gaymassage. Wellness. Kosmetik
Aufgabenstellung
Anfertigung eines Flyers, Anzeige und Aufkleber ....

```html
<!DOCTYPE html>
<html lang="de">
<head>
<meta charset="utf-8">
<title>Massage for Men – Flyer</title>
<link href="https://fonts.googleapis.com/css2?family=Fira+Sans:wght@500;600;700&display=swap" rel="stylesheet">
<style>
  :root {
    --orange: #f26a10;
    --white: #ffffff;
    --grey: #5f5f5f;
    --photo-dark: #6e4634;
    --photo-mid: #a7775d;
    --photo-light: #d9c0ae;
  }
  html, body { margin: 0; padding: 0; overflow: hidden; background: #fff; }
  .flyer {
    position: relative;
    width: 800px; height: 1200px;
    overflow: hidden;
    background: var(--white);
    font-family: "Fira Sans", sans-serif;
  }
  .hero-photo {
    position: absolute; left: 0; top: 0;
    width: 800px; height: 1000px;
    background: linear-gradient(180deg, var(--photo-dark) 0%, var(--photo-mid) 40%, var(--photo-light) 62%, #f4efeb 74%, var(--white) 88%);
  }
  .headline {
    position: absolute; left: 196px; width: 396px; top: 30px;
    color: var(--white); text-align: center;
    text-shadow: 0 2px 4px rgba(0,0,0,.35);
  }
  .headline .main { font-weight: 600; font-size: 92px; line-height: 1; letter-spacing: 1px; }
  .headline .rule { height: 2px; background: rgba(255,255,255,.8); margin: 12px 0; }
  .headline .sub { font-weight: 600; font-size: 46px; line-height: 1; }
  .headline .city { font-weight: 600; font-size: 75px; line-height: 1; }
  .side-contact {
    position: absolute; left: 64px; top: 24px;
    transform-origin: 0 0; transform: rotate(90deg);
    white-space: nowrap;
    font-weight: 500; font-size: 35px; line-height: 1;
    color: var(--white);
  }
  .side-contact .email { color: var(--orange); }
  .badge { position: absolute; left: 478px; top: 588px; width: 262px; height: 262px; }
  .services {
    position: absolute; left: 130px; width: 630px; top: 886px;
    text-align: center; color: var(--grey);
    font-weight: 600; font-size: 38px; line-height: 54px;
  }
  .hotline {
    position: absolute; left: 120px; width: 650px; top: 1006px;
    text-align: center; color: var(--orange);
    font-weight: 600; font-size: 64px; line-height: 1; letter-spacing: -1px;
  }
  .website {
    position: absolute; left: 120px; width: 650px; top: 1094px;
    text-align: center; color: var(--grey);
    font-weight: 600; font-size: 46px; line-height: 1;
  }
</style>
</head>
<body>
<div class="flyer">
  <div class="hero-photo" role="img" aria-label="Photo of a relaxed man lying on a massage table with hot stones on his back, candles in a warm spa room"></div>

  <div class="headline">
    <div class="main">MASSAGE</div>
    <div class="rule"></div>
    <div class="sub">FOR MEN BY MAN</div>
    <div class="rule"></div>
    <div class="city">IN MUNICH</div>
  </div>

  <div class="side-contact">Lindgasse 14 | München 80331 <span class="email">| info@velorin-point.com</span></div>

  <svg class="badge" viewBox="0 0 262 262" aria-label="Open daily">
    <circle cx="131" cy="131" r="122" fill="#fff" stroke="#f26a10" stroke-width="14"/>
    <g transform="rotate(-16 131 131)" fill="#f26a10" font-family="Fira Sans, sans-serif" font-weight="600" text-anchor="middle">
      <text x="131" y="122" font-size="62">OPEN</text>
      <line x1="52" y1="134" x2="210" y2="134" stroke="#f26a10" stroke-width="3"/>
      <text x="131" y="186" font-size="62">DAILY</text>
    </g>
  </svg>

  <div class="services">
    Seifenschaum • Glanzkörper<br>
    Intimrasur • Po Relax • Tantra
  </div>
  <div class="hotline">Hotline 0176/482 19 30</div>
  <div class="website">www.velorin-point.com</div>
</div>
</body>
</html>
```